Plakat-Design für ein großes, geistliches Konzert für Chor, Orchester und Solisten
Morvanta ist eine sehr kreative, zuverlässige und unkomplizierte Designerin und sehr zu empfehlen!
Zielgruppe
Wir sind eine Kantorei einer Kirchengemeinde, die in jedem Jahr ein großes Konzert für Chor, Orchester und Solisten veranstaltet. In diesem Jahr ist das Konzert in doppeltem Sinn etwas Besonderes. Zum einen weil wir das Konzert in Kooperation mit einer anderen Kantorei bestreiten und zum anderen weil die Anzahl der Mitwirkenden so groß ist, dass wir nicht der Kirche sondern das Konzert in die hiesige Stadthalle verlagern. Die Kirchenmusik präsentiert sozusagen sich außerhalb ihrer eigenen Mauern.
Eine Zielgruppe sollen diejenigen sein, die sich durch den besoneren Veranstaltungsort ansprechen lassen, also eher kirchenfremde Menschen. Das Plakat sollte auch das bestehende Stammpublikum nicht abschrecken, sondern einladen.
Es ist ein Folgeauftrag geplant, und zwar ein Programmheft/Textheft für das Konzert mit dem gleichen Design als Grundlage.
Aufgabenstellung
Das Plakat soll im DIN A3 oder A4 Hochformat erstellt werden.
Zwei weitere Logos von Förderern folgen noch.
Außer der Turm sind alle Logos von Förderern.
Der Turm ist sozusagen unser Markenzeichen und ein Wiedererkennungsmerkmal.
Das Konzert steht unter dem Motto: Von der Finsternis zum Licht.
Bezüglich der Textgröße sollte dieses Motto nicht größer sein als z.B. der Komponist und das Werk. Vielmehr soll das Motto durch ein grafisches Element eingearbeitet werden. 'Brauneckert' und 'Velmarung' sollen Eye catcher-Worte sein. Velmarung ist der Titel des Konzertes!

```html
<!DOCTYPE html>
<html lang="de">
<head>
<meta charset="utf-8">
<title>Von der Finsternis zum Licht – Konzertplakat</title>
<link href="https://fonts.googleapis.com/css2?family=Bebas+Neue&display=swap" rel="stylesheet">
<style>
:root{
  --stage:#a7a5a7;
  --night:#040307;
  --deep:#170d33;
  --violet:#2e1660;
  --magenta:#b0167f;
  --white:#ffffff;
  --blush:#ecc9e2;
  --ink:#1a1a1a;
}
*{margin:0;padding:0;box-sizing:border-box}
html,body{width:1200px;height:1200px;overflow:hidden;background:var(--stage)}
.poster{
  position:absolute;left:212px;top:51px;width:777px;height:1098px;overflow:hidden;
  box-shadow:0 4px 10px rgba(0,0,0,.25);
  background:linear-gradient(135deg, var(--night) 0%, #0b0620 35%, var(--deep) 62%, var(--violet) 100%);
  font-family:"Bebas Neue",sans-serif;color:var(--magenta);
}
.rays{position:absolute;left:0;top:0;width:777px;height:1002px}
.tower{position:absolute;left:14px;top:470px;width:202px;height:532px}
.program{position:absolute;left:250px;top:45px;font-size:30px;line-height:31px;letter-spacing:.2px;white-space:nowrap}
.program .hl{color:var(--white)}
.motto{position:absolute;left:35px;top:172px;font-size:120px;line-height:100px;letter-spacing:9px;font-weight:400;white-space:nowrap}
.motto .light{color:var(--white)}
.details{position:absolute;left:496px;top:494px;font-size:13px;line-height:15.3px;letter-spacing:.7px;text-transform:uppercase;white-space:nowrap}
.details p{margin-bottom:15.3px}
.details .label{color:var(--white)}
.date{position:absolute;left:35px;top:878px;font-size:29px;line-height:30px;letter-spacing:.3px;white-space:nowrap}
.date .hl{color:var(--white)}
.sponsors{position:absolute;left:0;top:1002px;width:777px;height:96px;background:var(--white)}
.sponsors .blush{position:absolute;left:0;top:0;width:262px;height:96px;background:var(--blush)}
.sponsor{position:absolute;top:0;height:96px;display:flex;align-items:center;font-family:"Bebas Neue",sans-serif;text-transform:uppercase;letter-spacing:.6px;white-space:nowrap}
.sponsor-church{left:262px;width:150px;gap:7px;font-size:15px;color:var(--magenta)}
.sponsor-church .mark{flex:none;width:10px;height:10px;border-radius:50%;background:var(--magenta)}
.sponsor-foundation{left:448px;width:160px;font-size:19px;line-height:20px;color:var(--ink)}
.sponsor-friends{left:636px;width:120px;font-size:19px;line-height:22px;color:var(--ink)}
</style>
</head>
<body>
<main class="poster">
  <svg class="rays" role="img" aria-label="Strahlenförmiges Lichtmuster aus Punkten, vom rechten Rand ausgehend" viewBox="0 0 777 1002" preserveAspectRatio="none">
    <defs>
      <radialGradient id="glow" cx="1" cy="0.49" r="0.75">
        <stop offset="0" stop-color="#c84a9c" stop-opacity=".55"/>
        <stop offset=".45" stop-color="#4b2c8a" stop-opacity=".3"/>
        <stop offset="1" stop-color="#000" stop-opacity="0"/>
      </radialGradient>
    </defs>
    <rect width="777" height="1002" fill="url(#glow)"/>
  </svg>

  <svg class="tower" role="img" aria-label="Silhouette des Kirchturms als Markenzeichen der Kantorei" viewBox="0 0 202 532" preserveAspectRatio="none">
    <defs>
      <linearGradient id="towerTone" x1="0" y1="0" x2="0" y2="1">
        <stop offset="0" stop-color="#6a2a8a" stop-opacity=".3"/>
        <stop offset="1" stop-color="#6a2a8a" stop-opacity=".45"/>
      </linearGradient>
    </defs>
    <rect width="202" height="532" fill="url(#towerTone)"/>
  </svg>

  <header class="program">
    <div>Anselm Brauneckert-<span class="hl">Torvaldi:</span> Choralkantate</div>
    <div>„Wer nur den lieben Gott lässt walten“</div>
    <div><span class="hl">Velmarung</span>-Sinfonie op. 52</div>
  </header>

  <h1 class="motto">
    <div>Von der</div>
    <div>Finsternis</div>
    <div class="light">Zum Licht</div>
  </h1>

  <section class="details">
    <p>Ilka Vornhaupt und<br>Mara-Lene Fesch<br><span class="label">Sopran</span><br>Jonas Trebbin<br><span class="label">Tenor</span></p>
    <p>Kammersymphonie Elbwald<br>Kirchenkreiskantorei Hollmark<br>Kantorei St. Ansgar, Wendelbruck</p>
    <p><span class="label">Gesamtleitung</span><br>Kirchenkreiskantoren<br>Peter Laudenbach (HOM)<br>und Tilman Oskamp (WB)</p>
    <p><span class="label">Einlass</span> 17.30 Uhr</p>
    <p><span class="label">Eintrittspreise</span><br>25,- / 20,- / 15,- Euro<br>(Ermässigungen 50%)</p>
    <p><span class="label">Kartenvorverkauf</span><br>Kulturverein Wendelbruck,<br>Lindenweg 7, 12345 WB</p>
    <p><span class="label">Weitere Informationen unter</span><br>www.ansgar-wendelbruck.de<br>www.kulturverein-wendelbruck.de<br>www.stadthalle-wendelbruck.de</p>
  </section>

  <div class="date">
    <div>Sonntag, <span class="hl">22.09.2019</span> um <span class="hl">18.00</span></div>
    <div><span class="hl">Uhr</span> in der Stadthalle Wendelbruck</div>
  </div>

  <footer class="sponsors">
    <div class="blush"></div>
    <div class="sponsor sponsor-church"><span class="mark"></span><span>Kirchenkreis Wendelbruck</span></div>
    <div class="sponsor sponsor-foundation"><span>Stiftung Landkreis<br>Wendelbruck</span></div>
    <div class="sponsor sponsor-friends"><span>Freundeskreis<br>Kirchenmusik</span></div>
  </footer>
</main>
</body>
</html>
```